We are looking for a simple design that would be uplifting for
upscale drug addicts

MERIDIAN COLLECTIVE

PLEASE SEE THE LINK FOR TAG LINE AND CONTENT

thank you.

here is all the actual info we need and we want something like this...

http://files.qzr.lumtrabox.example/rest/objects/7c2910e4b557d81a93e40bd59fa644163fe2adf0899f?uid=bdf8e1b9b6f556b6b83c44471fdc79%2fproofs&expires=1482716603&signature=kT9PwLmQxZbVoNHLdtrtlmoGHQB%3d

The shape and colors don't have to be like what I posted it is only an example.

Target Market(s)

Harlow Row, internet and creative types, men, early 30's,
upwardly mobile, drug addicts

current site

brightkestrelway.example

now launching new name Meridian Collective

Industry/Entity Type

Drug

Requirements
Must have
• upscale look, great font
Should not have
• a corporate look but should not look like a clinic.

```html
<!DOCTYPE html>
<html lang="en">
<head>
<meta charset="utf-8">
<title>Meridian Collective — Business Card</title>
<link href="https://fonts.googleapis.com/css2?family=Source+Sans+3:wght@400;600;700&display=swap" rel="stylesheet">
<style>
  :root {
    --brand-blue: #1f5fae;
    --deep-blue: #0b4a9c;
    --ink-grey: #4d4d4f;
    --text-dark: #2b2b2b;
    --card-white: #ffffff;
    --page-bg: #eef1f6;
    --wave-tint: #8fbbe8;
    --tint-light: #8fd0f5;
    --tint-mid: #1d79cf;
  }
  * { box-sizing: border-box; margin: 0; padding: 0; }
  html, body {
    width: 1200px;
    height: 927px;
    overflow: hidden;
    background: var(--page-bg);
    font-family: "Source Sans 3", "Helvetica Neue", Arial, sans-serif;
  }
  .canvas { position: relative; width: 1200px; height: 927px; }

  .card {
    position: absolute;
    width: 584px;
    height: 334px;
    overflow: hidden;
  }

  /* Front */
  .card-front { left: 179px; top: 122px; background: var(--card-white); }
  .wave-area {
    position: absolute;
    left: 0;
    top: 28px;
    width: 584px;
    height: 232px;
  }
  .wordmark {
    position: absolute;
    left: 58px;
    top: 22px;
    font-size: 56px;
    font-weight: 700;
    letter-spacing: -1.8px;
    color: var(--brand-blue);
    line-height: 1;
    white-space: nowrap;
  }
  .person { position: absolute; right: 33px; top: 92px; text-align: right; }
  .person-name { font-size: 28px; font-weight: 600; color: var(--brand-blue); line-height: 34px; }
  .person-title { font-size: 24px; color: var(--ink-grey); line-height: 30px; }
  .contact {
    position: absolute;
    left: 30px;
    top: 189px;
    font-size: 18px;
    color: var(--text-dark);
    line-height: 23.5px;
  }
  .contact .label { font-weight: 700; color: var(--brand-blue); }
  .contact .address { margin-top: 9px; }
  .site-front {
    position: absolute;
    right: 33px;
    top: 283px;
    font-size: 25px;
    line-height: 30px;
    font-weight: 700;
    color: var(--brand-blue);
  }

  /* Back */
  .card-back { left: 423px; top: 455px; background: var(--tint-mid); }
  .backdrop { position: absolute; left: 0; top: 0; width: 584px; height: 334px; }
  .tagline {
    position: absolute;
    left: 0;
    right: 0;
    top: 28px;
    text-align: center;
    color: #fff;
    font-size: 26px;
    line-height: 34px;
  }
  .site-band {
    position: absolute;
    left: 0;
    right: 0;
    bottom: 0;
    height: 56px;
    background: var(--deep-blue);
  }
  .site-back {
    position: absolute;
    right: 31px;
    bottom: 11px;
    color: #fff;
    font-size: 27px;
    line-height: 34px;
  }
</style>
</head>
<body>
<main class="canvas">

  <section class="card card-front" aria-label="Business card front">
    <svg class="wave-area" viewBox="0 0 584 232" preserveAspectRatio="none" role="img" aria-label="Flowing blue wave-line ornament sweeping across the card">
      <defs>
        <linearGradient id="wave-tone" x1="0" y1="0" x2="0" y2="1">
          <stop offset="0" stop-color="#8fbbe8" stop-opacity="0"/>
          <stop offset="0.45" stop-color="#8fbbe8" stop-opacity="0.22"/>
          <stop offset="0.6" stop-color="#8fbbe8" stop-opacity="0.22"/>
          <stop offset="1" stop-color="#8fbbe8" stop-opacity="0"/>
        </linearGradient>
      </defs>
      <rect x="0" y="60" width="584" height="120" fill="url(#wave-tone)"/>
    </svg>

    <div class="wordmark">Meridian Collective</div>

    <div class="person">
      <p class="person-name">First Lastname</p>
      <p class="person-title">Title</p>
    </div>

    <div class="contact">
      <p><span class="label">P:</span> 555.014.2280</p>
      <p><span class="label">F:</span> 555.014.2281</p>
      <p>email@brightkestrelway.example</p>
      <p class="address">418 Harlow Row, Suite 12<br>Eastbridge, ST 20417</p>
    </div>

    <p class="site-front">brightkestrelway.example</p>
  </section>

  <section class="card card-back" aria-label="Business card back">
    <svg class="backdrop" viewBox="0 0 584 334" preserveAspectRatio="none" role="img" aria-label="Radiating blue swirl pattern converging toward the lower centre">
      <defs>
        <radialGradient id="swirl-tone" cx="0.5" cy="0.85" r="0.85">
          <stop offset="0" stop-color="#a9dcf7"/>
          <stop offset="0.3" stop-color="#4aa6e6"/>
          <stop offset="0.7" stop-color="#1a6cc4"/>
          <stop offset="1" stop-color="#0f4fa3"/>
        </radialGradient>
      </defs>
      <rect width="584" height="334" fill="url(#swirl-tone)"/>
    </svg>

    <p class="tagline">We don't cut corners when it comes<br>to your longterm recovery.</p>

    <div class="site-band"></div>
    <p class="site-back">brightkestrelway.example</p>
  </section>

</main>
</body>
</html>
```